Book Cover "Venice"

Creation of a cover (14 x 20.5 cm + bleed area) for a book:
Image: “BrumeVerte” (Tiff joined)
AUTHOR: Corinne Valmer
TITLE: The murmurs of Lorient
PUBLISHER: Editions Pluvane (AT THE BOTTOM OF THE COVER)

Target Market(s)

Readers of romantic novels

Industry/Entity Type

Book

```html
<!DOCTYPE html>
<html lang="en">
<head>
<meta charset="utf-8">
<title>The Murmurs of Lorient — Cover</title>
<link rel="stylesheet" href="https://fonts.googleapis.com/css2?family=Francois+One&family=Cormorant+Garamond:wght@500&family=Open+Sans:wght@700&display=swap">
<style>
  :root {
    --stage: #ececec;
    --sky-top: #5a1420;
    --sky-mid: #c8261a;
    --sky-glow: #e8421c;
    --sky-low: #a3201a;
    --night: #1a0c10;
    --gold-light: #f2c644;
    --gold-deep: #cf9a2a;
    --ivory: #f3eee6;
  }
  html, body {
    margin: 0;
    width: 1200px;
    height: 819px;
    overflow: hidden;
    background: var(--stage);
  }
  .stage {
    position: relative;
    width: 1200px;
    height: 819px;
    display: flex;
    align-items: center;
    justify-content: center;
  }
  .cover {
    position: relative;
    width: 506px;
    height: 741px;
    overflow: hidden;
    box-shadow: 0 10px 30px rgba(0,0,0,0.18);
  }
  .cover-photo {
    position: absolute;
    inset: 0;
    background:
      linear-gradient(180deg, rgba(0,0,0,0) 62%, rgba(26,12,16,0.85) 82%, var(--night) 100%),
      radial-gradient(ellipse 90% 40% at 50% 62%, var(--sky-glow) 0%, rgba(232,66,28,0) 70%),
      linear-gradient(180deg, var(--sky-top) 0%, var(--sky-mid) 28%, var(--sky-low) 50%, var(--sky-mid) 66%, #6d1516 80%, var(--night) 100%);
  }
  .cover-title {
    position: absolute;
    top: 64px;
    left: 20px;
    right: 20px;
    margin: 0;
    text-align: center;
    font-family: "Francois One", sans-serif;
    font-weight: 400;
    text-transform: uppercase;
    line-height: 1;
    white-space: nowrap;
  }
  .cover-title span {
    display: block;
    background: linear-gradient(180deg, var(--gold-light) 0%, var(--gold-deep) 100%);
    -webkit-background-clip: text;
    background-clip: text;
    color: transparent;
  }
  .title-small { font-size: 70px; }
  .title-large { font-size: 108px; }
  .title-of { font-size: 72px; }
  .cover-author {
    position: absolute;
    left: 0;
    right: 0;
    bottom: 72px;
    margin: 0;
    text-align: center;
    font-family: "Cormorant Garamond", serif;
    font-weight: 500;
    font-size: 34px;
    letter-spacing: 2px;
    text-transform: uppercase;
    color: var(--ivory);
  }
  .cover-publisher {
    position: absolute;
    left: 0;
    right: 0;
    bottom: 36px;
    margin: 0;
    text-align: center;
    font-family: "Open Sans", sans-serif;
    font-weight: 700;
    font-size: 19px;
    letter-spacing: 1.5px;
    text-transform: uppercase;
    color: var(--ivory);
  }
</style>
</head>
<body>
  <div class="stage">
    <article class="cover">
      <div class="cover-photo" role="img" aria-label="Photograph of a blazing red sunset sky over a domed church silhouette and lit street lamps along the waterfront at dusk"></div>
      <h1 class="cover-title">
        <span class="title-small">The</span>
        <span class="title-large">Murmurs</span>
        <span class="title-of">of</span>
        <span class="title-large">Lorient</span>
      </h1>
      <p class="cover-author">Corinne Valmer</p>
      <p class="cover-publisher">Editions Pluvane</p>
    </article>
  </div>
</body>
</html>
```